Poster Design

Hello,

My name is Rowan Pickett and I run a vidora channel called 'CrumbleDiary'. I want a poster made for those who watch my video to purchase and put on their wall at home. The poster will be all text and as you can see, I've attached a few examples of posters which I would like it to be similar to. I use a lot of the colour #ab6f7f so it would be good to incorporate this in somewhere (maybe the background colour).
I would like the poster to say:
"Do More Of What Makes YOU Happy"
I need this poster to be for sale ready for christmas, so Im going to need the designs created as soon as possible. Im sorry for the rush.
Have fun with it and feel free to upload multiple versions of a design as well as a few designs if you like.
I look forward to seeing what you come up with.
Rowan
(Of course I will need to own all rights once the payment has been made)

```html
<!DOCTYPE html>
<html lang="en">
<head>
<meta charset="utf-8">
<title>Do More of What Makes You Happy – Poster</title>
<link rel="stylesheet" href="https://fonts.googleapis.com/css2?family=Alfa+Slab+One&family=Oswald:wght@400;500&family=Playfair+Display:ital@1&display=swap">
<style>
  :root {
    --frame: #eeb1ad;
    --mauve: #a66a7e;
    --turquoise: #82d8d8;
    --blush: #f0b7b1;
    --white: #ffffff;
  }
  * { margin: 0; padding: 0; box-sizing: border-box; }
  html, body { width: 800px; height: 1200px; overflow: hidden; background: var(--frame); }
  .poster {
    position: relative;
    width: 800px;
    height: 1200px;
    background: var(--frame);
    padding: 22px;
  }
  .poster__panel {
    position: relative;
    width: 100%;
    height: 100%;
    background: var(--mauve);
  }
  .line {
    position: absolute;
    left: 0;
    width: 756px;
    text-align: center;
    white-space: nowrap;
  }
  .line--do-more {
    top: 85px;
    font-family: "Alfa Slab One", serif;
    font-size: 102px;
    line-height: 1;
    color: var(--turquoise);
    letter-spacing: 0;
  }
  .divider {
    position: absolute;
    left: 0;
    top: 266px;
    width: 756px;
    height: 80px;
  }
  .line--of {
    top: 258px;
    font-family: "Playfair Display", serif;
    font-style: italic;
    font-size: 62px;
    line-height: 1;
    color: var(--white);
  }
  .line--what-makes {
    top: 360px;
    font-family: "Oswald", sans-serif;
    font-weight: 400;
    font-size: 126px;
    line-height: 1.1;
    color: var(--blush);
    letter-spacing: -2px;
  }
  .line--you {
    top: 558px;
    font-family: "Alfa Slab One", serif;
    font-size: 136px;
    line-height: 1;
    color: var(--turquoise);
  }
  .star {
    position: absolute;
    top: 578px;
    width: 80px;
    height: 80px;
  }
  .star--left { left: 93px; }
  .star--right { left: 593px; }
  .line--happy {
    top: 720px;
    font-family: "Alfa Slab One", serif;
    font-size: 178px;
    line-height: 1;
    color: var(--mauve);
    -webkit-text-stroke: 4px var(--white);
    text-shadow: 3px 3px 0 var(--white), 6px 6px 0 var(--white), 8px 9px 0 var(--white);
    letter-spacing: 2px;
  }
  .smile {
    position: absolute;
    left: 170px;
    top: 935px;
    width: 420px;
    height: 90px;
  }
  .line--channel {
    top: 1098px;
    font-family: "Oswald", sans-serif;
    font-weight: 500;
    font-size: 29px;
    line-height: 1;
    color: var(--white);
  }
</style>
</head>
<body>
  <main class="poster">
    <div class="poster__panel">
      <h1 class="line line--do-more">DO MORE</h1>

      <svg class="divider" viewBox="0 0 756 80" aria-hidden="true">
        <g fill="var(--white)">
          <rect x="100" y="10" width="218" height="3"/>
          <rect x="100" y="22" width="218" height="3"/>
          <rect x="100" y="35" width="218" height="3"/>
          <rect x="446" y="10" width="210" height="3"/>
          <rect x="446" y="22" width="210" height="3"/>
          <rect x="446" y="35" width="210" height="3"/>
        </g>
      </svg>
      <p class="line line--of">of</p>

      <p class="line line--what-makes">WHAT MAKES</p>

      <svg class="star star--left" viewBox="-40 -40 80 80" aria-hidden="true">
        <polygon fill="var(--turquoise)" points="0,-38 8,-19 27,-27 19,-8 38,0 19,8 27,27 8,19 0,38 -8,19 -27,27 -19,8 -38,0 -19,-8 -27,-27 -8,-19"/>
      </svg>
      <p class="line line--you">YOU</p>
      <svg class="star star--right" viewBox="-40 -40 80 80" aria-hidden="true">
        <polygon fill="var(--turquoise)" points="0,-38 8,-19 27,-27 19,-8 38,0 19,8 27,27 8,19 0,38 -8,19 -27,27 -19,8 -38,0 -19,-8 -27,-27 -8,-19"/>
      </svg>

      <p class="line line--happy">happy</p>

      <svg class="smile" viewBox="0 0 420 90" aria-hidden="true">
        <g fill="none" stroke="var(--white)" stroke-width="5" stroke-linecap="round">
          <path d="M18 28 Q210 130 402 28"/>
          <path d="M8 20 L26 36"/>
          <path d="M412 20 L394 36"/>
        </g>
      </svg>

      <p class="line line--channel">vidora.example/CrumbleDiary</p>
    </div>
  </main>
</body>
</html>
```